Northridge Valley Arms Banner

We are looking for a banner ad that we will run on DawnPostly.com the size is 758x120 and also a matching one that is 300x250 can be animated or static.final graphics will need to be submitted in jpg, gif or similar format. Our shop is a firearms business called "Northridge Valley Arms" located at 412 Route 19 South, Pellham Ms. 38412 phone is 662-574-3108 . it need to be modern and eye catching and be more geared to the tactical side. Our website is
northridgevalarms.com the banners DO NOT have to match website. would like a DIFFERENT LOOK than my website

```html
<!DOCTYPE html>
<html lang="en">
<head>
<meta charset="utf-8">
<title>Northridge Valley Arms – Banner Set</title>
<link rel="stylesheet" href="https://fonts.googleapis.com/css2?family=Titillium+Web:wght@400;600;700&display=swap">
<style>
  :root {
    --canvas: #e4e5e7;
    --panel-dark: #17181a;
    --panel-dark-2: #2a2b2e;
    --green-light: #8fb51c;
    --green-mid: #5d8a12;
    --green-deep: #1f2d0c;
    --edge: #b9bcbf;
    --gold: #f2c21a;
    --white: #ffffff;
    --steel-light: #d9dadb;
    --steel-dark: #6f7275;
  }
  * { box-sizing: border-box; margin: 0; padding: 0; }
  html, body { width: 1200px; height: 1200px; overflow: hidden; }
  body {
    background: var(--canvas);
    font-family: "Titillium Web", Arial, sans-serif;
    position: relative;
  }
  .banner {
    position: absolute;
    overflow: hidden;
    background: linear-gradient(135deg, var(--panel-dark-2) 0%, var(--panel-dark) 60%);
    border: 2px solid var(--edge);
  }
  .banner svg.backdrop { position: absolute; inset: 0; width: 100%; height: 100%; }

  .brand {
    position: absolute;
    display: flex;
    align-items: center;
    gap: 12px;
  }
  .brand-dot {
    flex: none;
    width: 44px; height: 44px;
    border-radius: 50%;
    background: var(--green-mid);
  }
  .brand-name {
    color: var(--gold);
    font-weight: 700;
    line-height: 1.02;
  }

  .headline { position: absolute; color: var(--white); font-weight: 700; line-height: 1.1; }
  .details  { position: absolute; color: var(--gold); font-weight: 600; line-height: 1.3; white-space: nowrap; }

  .product-photo {
    position: absolute;
    border-radius: 10px;
    background: linear-gradient(160deg, var(--steel-light) 0%, #a9abad 55%, var(--steel-dark) 100%);
  }

  /* 758 x 120 leaderboard */
  .banner-wide { left: 62px; top: 310px; width: 1078px; height: 170px; }
  .banner-wide .brand { left: 28px; top: 52px; }
  .banner-wide .brand-name { font-size: 28px; width: 200px; }
  .banner-wide .headline { left: 430px; top: 18px; font-size: 29px; }
  .banner-wide .details { left: 480px; top: 66px; font-size: 18px; text-align: center; width: 260px; }
  .banner-wide .product-photo { left: 826px; top: 14px; width: 206px; height: 140px; }

  /* 300 x 250 medium rectangle */
  .banner-box { left: 382px; top: 600px; width: 438px; height: 362px; }
  .banner-box .brand { left: 18px; top: 20px; }
  .banner-box .brand-name { font-size: 24px; width: 190px; }
  .banner-box .headline { right: 24px; top: 130px; font-size: 36px; text-align: right; }
  .banner-box .details { right: 24px; top: 268px; font-size: 17px; text-align: right; }
  .banner-box .product-photo { left: 20px; top: 200px; width: 132px; height: 136px; }
</style>
</head>
<body>

<section class="banner banner-wide" aria-label="Leaderboard banner">
  <svg class="backdrop" viewBox="0 0 1078 170" preserveAspectRatio="none" aria-hidden="true">
    <defs>
      <linearGradient id="wideGreen" x1="0" y1="0" x2="1" y2="1">
        <stop offset="0" stop-color="#9cc21f"/>
        <stop offset="0.55" stop-color="#5d8a12"/>
        <stop offset="1" stop-color="#2c4110"/>
      </linearGradient>
    </defs>
    <path d="M352,0 Q380,110 442,170 L1078,170 L1078,0 Z" fill="url(#wideGreen)" stroke="#b9bcbf" stroke-width="4"/>
  </svg>
  <div class="brand">
    <span class="brand-dot"></span>
    <span class="brand-name">Northridge Valley Arms</span>
  </div>
  <h1 class="headline">Northridge Valley Arms</h1>
  <p class="details">located at 412 Route 19 South,<br>Pellham Ms. 38412<br>Phone is 662-574-3108</p>
  <div class="product-photo" role="img" aria-label="Photo of a stainless semi-automatic pistol"></div>
</section>

<section class="banner banner-box" aria-label="Medium rectangle banner">
  <svg class="backdrop" viewBox="0 0 438 362" preserveAspectRatio="none" aria-hidden="true">
    <defs>
      <linearGradient id="boxGreen" x1="0" y1="0" x2="0" y2="1">
        <stop offset="0" stop-color="#9cc21f"/>
        <stop offset="0.55" stop-color="#4f7711"/>
        <stop offset="1" stop-color="#1a220d"/>
      </linearGradient>
    </defs>
    <path d="M438,98 L230,100 Q70,120 10,362 L438,362 Z" fill="url(#boxGreen)" stroke="#b9bcbf" stroke-width="4"/>
  </svg>
  <div class="brand">
    <span class="brand-dot"></span>
    <span class="brand-name">Northridge Valley Arms</span>
  </div>
  <h2 class="headline">Northridge<br>Valley<br>Arms</h2>
  <p class="details">located at 412 Route 19 South,<br>Pellham Ms. 38412<br>Phone is 662-574-3108</p>
  <div class="product-photo" role="img" aria-label="Photo of a stainless semi-automatic pistol"></div>
</section>

</body>
</html>
```